Brochure for financial company

Follow our brand guidelines to design a 12-15 page full color brochure including all our copy. We need it laid out in a professional look and feel and print ready. We have included our brand guidelines which must be followed, in addition to samples of our folder and notecards which are already in use. We can provide example pictures of our existing brochure which we like but is prior to our brand change.

Target Market(s)

Baby Boomers 50+

Industry/Entity Type

Financial Planning

Requirements
Must have
• Look and feel similar to our website www.brantwellfinancial.com follows our brand guidelines. Stock photos must represent our clientele 50+
Nice to have
• A good layout and flow. We have samples of our previous brochure if needed. We recently rebranded so we're updating / revising our brochure.

```html
<!DOCTYPE html>
<html lang="en">
<head>
<meta charset="utf-8">
<title>Brantwell Financial Brochure Spreads</title>
<link href="https://fonts.googleapis.com/css2?family=Crimson+Text:ital,wght@0,400;0,600;0,700;1,400;1,600&display=swap" rel="stylesheet">
<style>
:root{
  --backdrop:#dcdcdc;
  --paper:#ffffff;
  --ink:#3a3a3a;
  --navy:#1c3a5e;
  --navy-deep:#1a3558;
  --khaki:#b3a57a;
  --numeral:#c9c9c9;
  --teal:#2cc4b4;
  --lime:#bccd1c;
  --orange:#f17c1f;
  --red:#e2183e;
  --purple:#7c3ea9;
  --step-magenta:#e0266c;
  --step-amber:#f5a823;
  --step-violet:#6b3c97;
  --royal:#0a5ce8;
}
*{box-sizing:border-box;margin:0;padding:0}
html,body{width:1200px;height:1200px;overflow:hidden}
body{background:var(--backdrop);font-family:"Crimson Text",Georgia,serif;color:var(--ink);position:relative}
.spread{position:absolute;width:528px;height:376px;background:var(--paper);box-shadow:0 2px 6px rgba(0,0,0,.25);overflow:hidden}
.spread-a{left:36px;top:16px}
.spread-b{left:637px;top:16px}
.spread-c{left:36px;top:412px}
.spread-d{left:637px;top:412px}
.spread-e{left:296px;top:806px}
.blk{position:absolute}
p{font-size:4.3px;line-height:1.42;margin-bottom:3px;text-align:justify}
.head-sm{font-size:6.2px;font-weight:700;color:var(--navy);margin-bottom:2.5px;line-height:1.2}
.head-lg{font-size:10.5px;font-weight:600;color:var(--navy);letter-spacing:.5px;text-transform:uppercase;line-height:1.15;margin-bottom:3px}
.photo{position:absolute}
.navy-panel{background:var(--navy);color:#fff;padding:7px 22px}
.navy-panel p{color:#e8ecf2}
.navy-panel .head-sm{color:#fff}
.numeral{position:absolute;left:20px;font-size:30px;color:var(--numeral);line-height:1}
.case-bar{position:absolute;left:42px;width:208px;color:#fff;font-size:3.9px;line-height:1.4;padding:4px 8px;display:flex;align-items:center;text-align:justify}
.band{position:absolute;left:286px;width:220px;color:#fff;text-align:center;padding:5px 12px 10px;clip-path:polygon(0 0,50% 8%,100% 0,100% 86%,50% 100%,0 86%)}
.band.first{clip-path:polygon(0 0,100% 0,100% 86%,50% 100%,0 86%)}
.band h4{font-size:4.2px;font-weight:700;margin:3px 0 2px}
.band p{font-size:3.8px;color:#fff;text-align:center;line-height:1.4}
.frameworks{display:grid;grid-template-columns:repeat(3,1fr);font-size:4.3px;row-gap:6px;margin:4px 0 8px}
.frameworks span::before{content:"· "}
.khaki-panel{background:var(--khaki);padding:8px 22px}
.khaki-panel .head-sm{color:#2d2d2d}
.khaki-panel p{color:#2e2a20}
.alloc{position:absolute;font-size:3.9px;line-height:1.42}
.alloc b{font-weight:400}
.royal-block{position:absolute;left:118px;top:32px;width:409px;height:138px;background:var(--royal)}
.royal-block-text{color:#fff}
.royal-block-text p{color:#eef3ff}
.head-mid{font-size:8.6px;font-weight:600;color:var(--navy);line-height:1.18;margin-bottom:4px}
.quote-panel{position:absolute;left:150px;top:294px;width:376px;height:82px;background:var(--navy-deep);padding:11px 20px 0 22px;color:#fff}
.quote-panel blockquote{font-size:6px;font-weight:700;line-height:1.3;text-align:justify}
.quote-panel cite{display:block;text-align:right;font-size:5px;font-style:italic;margin-top:6px}
.gold-strip{position:absolute;left:270px;top:0;width:7px;height:376px;background:var(--khaki)}
</style>
</head>
<body>

<!-- Spread: technology, communication, planning process -->
<section class="spread spread-a">
  <div class="blk" style="left:22px;top:18px;width:222px">
    <h3 class="head-sm">Technology Portals/ Electronic &amp; Hard Copy Statements/ Cybersecurity</h3>
    <p>Brantwell Financial partners with the largest custodians within the financial industry. Independent custodians such as Harbor Lane Securities, Northgate Custody, Crestmark Trading or Ashby &amp; Cole act in a similar manner as a standard bank account. Clients who wish to do so may register to review their account in real-time through a custodian's online portal or, in certain instances, through a downloadable app for a smartphone or tablet. Furthermore, clients may select whether to receive trade confirmations and statements online or by traditional mail delivery. Regardless of the level from which you choose to engage technology, reviewing your account at any time is extremely easy and efficient. Often, clients of Brantwell Financial will utilize more than one custodian for security purposes.</p>
    <p>Cybersecurity has become one of the most critical concerns within the investment advisory world. Within the walls of Brantwell Financial we're proud to follow rigorous security measures required by our regulatory organizations in addition to the active and ongoing due diligence of our partners' security measures specifically our client custodians. Often we may suggest utilizing more than one custodian in order to diversify security risks for client accounts. Brantwell Financial is to our knowledge one of the only fee-only advisors suggesting clients split custodians among their investment portfolios, a theme we believe will become a best practice in the near future.</p>
  </div>
  <div class="blk navy-panel" style="left:0;top:160px;width:264px;height:98px">
    <h3 class="head-sm">Ongoing Client Communication</h3>
    <p>Brantwell Financial prides itself on continually educating its clientele through informative and engaging emails, newsletters, blog posts and media archives. It is our intent to assist you with your financial goals while helping you to understand today's complex investment and economic world. Successful client education correlates with confidence in our investment strategies, often leading to client referrals, which remain our fastest and preferred method of growth.</p>
    <h3 class="head-sm" style="margin-top:5px">Personalized Portfolio &amp; Planning Reviews</h3>
    <p>Several times throughout the year Brantwell Financial will reach out to you via telephone or email to review your personal situation or to just say "Hello." Often this dialog simply results in strengthening our relationship, however if needed, also aids in scheduling periodic portfolio and plan reviews to discuss goals and objectives.</p>
  </div>
  <div class="blk" style="left:22px;top:268px;width:222px">
    <h2 class="head-lg">Financial / Retirement Planning Process</h2>
    <p>What is the first thing you do when you jump in the car for a long drive? More than likely you fire up the GPS on your phone or maybe you take out the map or printed directions. Regardless of your medium, the most critical piece of the equation before you set off on any journey is a solid set of directions. While this points you in the right direction, it is also something you refer to many times throughout your trip to ensure that you're still on course, and it also gives a good idea of what time you'll arrive. Along the way, there will be unforeseen challenges, traffic jams, inclement weather, and the occasional detour. These encounters force you to consult your map, possibly adjust your coordinates and maybe even establish a different route.</p>
  </div>
  <div class="blk" style="left:286px;top:22px;width:222px">
    <p>Over the years, Brantwell Financial has learned that navigating a journey and successful financial advising are very similar. In order to achieve your specific financial goal, you must have a proper plan en route. Once this plan is developed and implemented, in order to achieve success, it must be constantly evaluated.</p>
    <h3 class="head-sm" style="margin-top:5px">What is your required rate of return?</h3>
    <p>Whenever we have the privilege of meeting clients to discuss their financial affairs, we always start with what we believe to be the most important question. What is the rate of return required to achieve your goal? Until this is identified, an investment plan is nearly impossible to implement. It is only after the required rate of return is calculated that we can suggest an appropriate risk allocation that has historically achieved the desired results. While on occasion an individual's required rate of return and risk allocation matches their risk temperament, it is not always the case.</p>
    <h3 class="head-sm" style="margin-top:5px">What is your Risk Temperament?</h3>
    <p>Historically, portfolio allocation and risk have correlated with age. Most believe that the younger an investor, the more risk they should take. The theory goes that, given more time, it is easier to make up losses. At Brantwell Financial we believe that every person has a unique risk temperament that may or may not correlate with the standard age-based risk model. While our planning process helps us determine your required rate of return and therefore suggests an appropriate risk allocation, if this does not match your risk temperament, adjusting goals and re-evaluating the overall financial plan may be required.</p>
  </div>
  <div class="photo" role="img" aria-label="Photo of a retired couple relaxing on a lakeside dock" style="left:286px;top:172px;width:242px;height:182px;background:linear-gradient(160deg,#6f8f3a 0%,#9bb35a 35%,#5d7a3e 60%,#8a7a52 100%)"></div>
</section>

<!-- Spread: case study and planning steps -->
<section class="spread spread-b">
  <div class="blk" style="left:22px;top:24px;width:230px">
    <h2 class="head-lg" style="margin-bottom:0">Case Study</h2>
    <div style="font-size:3.6px;color:#555">Required Rate of Return Discovery Process</div>
  </div>
  <div class="numeral" style="top:50px">1</div>
  <div class="case-bar" style="top:44px;height:52px;background:var(--teal)">Joe and Sue are small business owners in their early 50s. Their cumulative income is over $200,000 per year and they are investing the maximum amount into corporate retirement plans, which are also being matched up to 6%. In addition to their corporate retirement plan, they have a profit sharing component which has allowed them to save an additional $500,000 in tax deferred income. Their only debt is a mortgage, which is scheduled to be paid off within the next 5 years.</div>
  <div class="numeral" style="top:106px">2</div>
  <div class="case-bar" style="top:104px;height:30px;background:var(--lime)">Age-based risk tolerance may suggest a stock/ bond allocation for Joe and Sue in the moderately aggressive range with a potential exposure to stocks of up to 60 or 70%.</div>
  <div class="numeral" style="top:145px">3</div>
  <div class="case-bar" style="top:144px;height:30px;background:var(--orange)">While they have followed this standard allocation for years, they have also started to become increasingly concerned over the recent advancement in the stock market and the future uncertainty of the economy.</div>
  <div class="numeral" style="top:183px">4</div>
  <div class="case-bar" style="top:182px;height:29px;background:var(--red)">After completing a LIFE plan from Brantwell Financial Joe and Sue realized that to meet their long term financial goals and provide the necessary income they're looking for within retirement, their required rate of return is approximately 2.5%, much lower than ever anticipated.</div>
  <div class="numeral" style="top:220px">5</div>
  <div class="case-bar" style="top:219px;height:30px;background:var(--purple)">Using historical market rates of return within the stock market and bond market, it came to their attention that they could lower their stock market exposure considerably and remain on track to achieve their investment and retirement objectives.</div>
  <div class="blk" style="left:22px;top:262px;width:230px">
    <h2 class="head-lg">Classical Investment Management</h2>
    <p>Over the years investment management as a profession has evolved from one in which the adviser took an active interest in making educated decisions within the financial markets to one in which a salesperson began marketing outsourced products which often include high cost, internal fees, paying enormously high commissions.</p>
    <p>Conflict of interests have replaced fiduciary obligations, and up-front commissions have taken the place of mutually agreed upon fees for service and performance.</p>
    <p>Brantwell Financial prides itself on a return to a classical model whereby revenue is derived from a fixed fee for management of money and on occasion, from our LIFE plan process. We are not fee-based, claiming to provide fee services supplemented by commissionable products but rather fee-only where our interests align with those of our clients and possess zero conflict.</p>
  </div>
  <h2 class="blk head-lg" style="left:286px;top:24px">Financial Planning Process</h2>
  <div class="band first" style="top:40px;height:70px;background:var(--teal)">
    <h4>Step 1: Life Plan Questionnaire</h4>
    <p>Our process begins by completing our LIFE plan questionnaire. This confidential, fact finding document helps us to analyze such things as your current balance sheet, liquidity position, cash flow needs, future tax liabilities and retirement income needs. Once completed, we use the data to present a drafted, multi-page, hardcover, bound plan.</p>
  </div>
  <div class="band" style="top:104px;height:66px;background:var(--lime)">
    <h4 style="margin-top:6px">Step 2: Plan Presentation</h4>
    <p>Whether it is in our office, or via a conference call or web interface, the plan presentation is something we take very seriously. It is our goal through this time to educate our clients on precisely how their financial plan looks and what it says in plain English. This meeting takes approximately 1 – 2 hours.</p>
  </div>
  <div class="band" style="top:164px;height:72px;background:var(--step-magenta)">
    <h4 style="margin-top:6px">Step 3: Recommendations &amp; Implementation</h4>
    <p>At the conclusion of the plan presentation, we will review with each client our recommendations based purely on the desires and goals set forth from the very beginning. Often we find that an individual's life goals do not correlate with their current investment allocations, savings rate or overall balance sheet. At times there can be tough conversations as we seek to present the truth in an unbiased and purely fiduciary fashion, then explore the methods by which income will be distributed.</p>
  </div>
  <div class="band" style="top:230px;height:64px;background:var(--step-amber)">
    <h4 style="margin-top:6px">Step 4: Ongoing Plan Revision</h4>
    <p>A true financial plan is not stagnant but rather a living, breathing document which is adjusted and adapted as your life changes. Depending on each client's situation, we take great pride in revising and updating financial plans on an as needed basis. Typically, we update plans every two years prior to retirement, a few months before retirement and annually thereafter.</p>
  </div>
  <div class="band" style="top:288px;height:62px;background:var(--step-violet)">
    <h4 style="margin-top:6px">Step 5: Communication &amp; Education</h4>
    <p>Our best client is the one who can knowledgeably speak about his or her own financial future and the finite steps we are taking to achieve their goals. At Brantwell Financial, we reach out to our clients each quarter to touch base and discuss how the plan is progressing and our firm's philosophies with whom they have partnered.</p>
  </div>
</section>

<!-- Spread: investment management and risk tolerance -->
<section class="spread spread-c">
  <div class="photo" role="img" aria-label="Photo of business hands reviewing printed charts" style="left:0;top:0;width:264px;height:118px;background:linear-gradient(120deg,#1e2c44 0%,#3b5578 45%,#9fb4cf 70%,#2b3a52 100%)"></div>
  <div class="blk" style="left:22px;top:134px;width:222px">
    <h2 class="head-lg">Investment Management</h2>
    <p>For centuries select individuals have been successfully navigating the financial markets and understanding the intricacies of what moves a market over shorter durations such as weeks and months. While fundamental analysis and corporate valuation will always prevail over longer time periods such as decades, markets often remain irrational and volatile, ebbing and flowing based on nothing more than human emotion and the key variables that will always be present – fear and greed.</p>
    <p>At Brantwell Financial we are not afraid of the word 'sell' and we will often use cash as our best hedge against market volatility or market loss. Furthermore, we pride ourselves on an active management style that always seeks to capitalize on the market's irrationality. On a regular basis we are evaluating countless investment opportunities such as sectors of interest, individual companies or general economic themes. Gaining an understanding for what is happening under the surface such as sector relative strength, market leadership and general market direction is crucial. Our goal is to find opportunities within the diverse market landscape which we feel comfortable owning for a long time.</p>
    <h3 class="head-sm" style="margin-top:6px">Keys to Investment Success</h3>
    <div style="font-size:4.3px;font-weight:700;color:#222;margin-bottom:3px">Risk Temperament → Asset Allocation → Diversification → Rebalancing → Time</div>
    <p>Over the years, investment themes have come and gone while five basic tenets have remained consistent. At Brantwell Financial, we take these tenets very seriously as they provide the foundation upon which we build and manage our clients' financial assets. We realize that without all five investment variables in place, an individual runs the risk of significantly altering their financial future and missing the goal set forth from the beginning.</p>
    <p>Selecting an adviser in today's world of provocative and enticing investment themes has become an increasingly challenging task. At Brantwell Financial, we do not trumpet a new or unique style of investing; rather, we simply adhere to basic methods that have been proven to meet financial goals since the earliest days of the capital markets.</p>
  </div>
  <div class="blk" style="left:286px;top:22px;width:222px">
    <h3 class="head-sm">Risk Tolerance / Temperament</h3>
    <p>Traditionally labeled only Risk Tolerance and correlating with one's age, at Brantwell Financial we believe it is critical that an individual's risk tolerance match their personal temperament in order to properly handle the emotional ups and downs of the financial markets. Individuals possess their own unique risk temperament which is crucial to explore from both a quantitative and qualitative angle before proceeding with any investment strategy.</p>
    <p>Financial markets follow cyclical patterns and often advance for a number of years, and then retreat for a number of years. Furthermore, financial markets occasionally experience significant and unforeseen corrections. The most recent being the financial crisis of 2008 and 2009, which negatively impacted all financial markets for more than a calendar year. The extent to which one's portfolio will participate in a bearish market cycle will always be determined by that individual's tolerance for risk. Investors who understand that financial markets are cyclical in nature, and that financial downturns will take place, achieve their desired financial goals while exposing assets within a comfortable investment framework.</p>
    <h3 class="head-sm" style="margin-top:6px">Investment Frameworks</h3>
    <div class="frameworks">
      <span>Stable Value</span><span>Balanced</span><span>Moderately Aggressive</span>
      <span>Conservative</span><span>Traditional 60/40</span><span>Aggressive</span>
    </div>
    <p>An investor will discover that his goals, unique personality and past experience are instrumental in developing an appropriate risk level. Determining an individual investor's risk tolerance is a primary foundational step in determining proper portfolio asset allocation. Once risk tolerance has been determined, an individual can be classified within one of the risk framework categories, an important and primary stage within the investment strategy process.</p>
  </div>
  <div class="blk khaki-panel" style="left:264px;top:230px;width:264px;height:146px">
    <h3 class="head-sm">Asset Allocation</h3>
    <p>Sometimes, old sayings such as "don't put all your eggs in one basket" possess such simple yet profound morsels of wisdom that investors dare not overlook. One of the most basic, yet ignored, principles of successful investing is properly allocating investments among different asset classes. Asset allocation is commonly mistaken with diversification however the two are quite different.</p>
    <p>At Brantwell Financial, when we discuss Asset Allocation we are referring to the blend between variable asset classes, such as stocks and fixed asset classes, such as bonds. Not only is it important to properly define this investment trait, but it is also crucial to implement and adhere to a prudent asset allocation strategy in order to achieve the desired results.</p>
    <p>Once an individual's risk tolerance has been identified and matched with an investment framework, a target asset allocation is determined and the Brantwell Financial investment process is set into motion.</p>
  </div>
</section>

<!-- Spread: allocation categories and frameworks -->
<section class="spread spread-d">
  <div class="royal-block"></div>
  <h3 class="blk head-sm" style="left:22px;top:20px;font-size:5.4px">The categories of the Brantwell Financial asset allocations are as follows:</h3>
  <div class="alloc" style="left:22px;top:36px;width:88px">Stable Value:<br>100% Fixed<br>Investments including Cash, CDs, Government and Corporate Bonds</div>
  <div class="alloc" style="left:22px;top:76px;width:88px">Balanced:<br>50% Exposure to the current Brantwell Financial Equity Allocation<br>50% Fixed Investments including Cash, CDs, Government &amp; Corporate Bonds</div>
  <div class="alloc" style="left:22px;top:130px;width:88px">Moderately Aggressive:<br>70% Exposure to the current Brantwell Financial Equity Allocation<br>30% Fixed Investments including Cash, CDs, Government &amp; Corporate Bonds</div>
  <div class="alloc royal-block-text" style="left:126px;top:40px;width:124px">Conservative:<br>30% Exposure to the current Brantwell Financial Equity Allocation<br>70% Fixed Investments including Cash, CDs, Government and Corporate Bonds</div>
  <div class="alloc royal-block-text" style="left:126px;top:88px;width:124px">Traditional 60/40<br>60% Exposure to the current Brantwell Financial Equity Allocation<br>40% Fixed Investments including Cash, CDs, Government and Corporate Bonds</div>
  <div class="alloc royal-block-text" style="left:126px;top:140px;width:124px">Aggressive:<br>100% Exposure to the current Brantwell Financial Equity Allocation</div>
  <div class="blk" style="left:22px;top:182px;width:228px">
    <h2 class="head-mid">Additional Investment Frameworks (Dividend Income / Sector Alpha Index / Municipal or Corporate Ladder)</h2>
    <h3 class="head-sm" style="font-size:5.6px">Dividend Income:</h3>
    <p>On occasion, clients may require additional income through equity dividends rather than fixed income. In certain instances a dividend income strategy may also be suggested as part of an overall equity allocation. In addition to our standard investment frameworks, Brantwell Financial offers a dividend income model consisting of approximately 30-40 individual equities which fit our proprietary financial requirements for long term dividend centered investment. By nature of the Dividend Income equity allocation, this portfolio is 100% stocks and therefore classified as 'Aggressive' and is benchmarked against the Meridian Dividend Index, following a relative market approach, seeking dividend income from equity exposure.</p>
    <p>At times volatility within this allocation may be higher than standard investment frameworks and possess a higher market correlation over the short to medium term.</p>
    <h3 class="head-sm" style="font-size:5.6px;margin-top:4px">Sector Alpha Index (Institutional)</h3>
    <p>For our institutional clients who seek the lowest possible investment management fees available within the institutional marketplace and relative market correlation Brantwell Financial is proud to offer our Sector Alpha Index portfolio. This unique approach to equity allocation seeks to provide portfolio alpha through the reweighting of traditional index market sectors through fundamental and other proprietary research indicators. Please see our Sector Alpha Index material specific for this portfolio.</p>
  </div>
  <h3 class="blk head-sm" style="left:286px;top:20px;font-size:5.6px">Municipal or Corporate Bond Ladders</h3>
  <div class="blk royal-block-text" style="left:286px;top:38px;width:224px">
    <p>In partnership with leading fixed income managers, Brantwell Financial offers select clients access to individual fixed income bond laddered portfolios through such companies as Stonebridge Fixed Income or Larkfield Capital. With competitive third-party pricing and SMA custodian relationships, clients have access to individual bonds traditionally only available to the large institutions and extreme high net worth clients. More information including customized investment plans may be provided upon request.</p>
    <h3 class="head-sm" style="color:#fff;font-size:5.6px;margin-top:3px">Diversification:</h3>
    <p>As financial markets move through normal and healthy business cycles, variable asset classes become both more attractive and less attractive. While one may be able to improve investment results attempting to determine the business cycle we are in and allocating investments accordingly, it has been proven that with proper diversification or exposure to a multiple number of variable asset classes, not only can individuals improve results, but they can also reduce portfolio volatility.</p>
    <p>At Brantwell Financial, we take diversification very seriously and pursue a rigorous process of selecting the proper variable asset classes, and determining the prudent exposure to each. This allocation is called the Brantwell Financial Equity Allocation, and is diversified among such variable asset classes as large and small capitalized domestic companies, international and emerging markets, as well as potential exposure to sector specific areas such as gold or materials.</p>
  </div>
  <div class="blk" style="left:286px;top:176px;width:224px">
    <p>Once the Brantwell Financial Equity Allocation has been determined, clients and their investment portfolios are exposed to this in direct correlation to their investment framework, which will be determined by their risk tolerance.</p>
  </div>
  <div class="photo" role="img" aria-label="Photo of seedlings growing from rising stacks of coins in soil" style="left:265px;top:208px;width:263px;height:168px;background:linear-gradient(135deg,#2f5a1e 0%,#7da83e 40%,#c9b46a 65%,#4a3a24 100%)"></div>
</section>

<!-- Spread: rebalancing and time -->
<section class="spread spread-e">
  <div class="blk" style="left:22px;top:22px;width:236px">
    <h3 class="head-sm">Rebalancing</h3>
    <p>Over time as a portfolio is exposed to the natural fluctuations that occur within financial markets, the asset allocation and diversified nature of the portfolio will also change. Due to the historical truth that at different times, different asset classes will outperform others, it is extremely important for a portfolio to be rebalanced in order to maintain the desired allocation.</p>
    <p>On an annual basis, or more frequently if needed, Brantwell Financial systematically rebalances each portfolio by calculating the current allocation and adjusting the exposure accordingly.</p>
    <p>For example, during a given year where the stock market has performed particularly well, a portfolio allocation seeking a mix of 60% stocks and 40% fixed income, may become skewed as high as 70% variable assets and 30% fixed income. It is critical for us to rebalance this weighting and thus reweight the portfolio back to its intended 60%/40% allocation, thus taking profits from the equities in a systematic and pre-planned manner.</p>
  </div>
  <div class="photo" role="img" aria-label="Photo of balanced stacked pebbles on a sunlit shore" style="left:0;top:142px;width:258px;height:234px;background:linear-gradient(170deg,#e9eef2 0%,#c7d2da 40%,#9a8b76 70%,#6c5f50 100%)"></div>
  <div class="gold-strip"></div>
  <div class="photo" role="img" aria-label="Photo of rising stacks of coins beside a stopwatch" style="left:277px;top:0;width:251px;height:158px;background:linear-gradient(120deg,#1c1c1c 0%,#3a3a38 40%,#a8894a 70%,#2a2a28 100%)"></div>
  <div class="blk" style="left:286px;top:170px;width:222px">
    <h3 class="head-sm">Time</h3>
    <p>Entering into a relationship with an investment adviser should not be taken lightly, and the success of an investment strategy can only be determined after navigating a series of financial market cycles. Unfortunately, while it would be wonderful to experience success immediately, this is not always the case. Prudent and disciplined investors can, however, significantly improve results if they remain patient while diligently adhering to the developed plan.</p>
    <p>Unfortunately, most advisers don't have a proper plan in place and individuals are sent wandering through the financial landscape without a guide. While the development of such a plan is crucial, allowing adequate time for this plan to work is also vitally important.</p>
    <p>Brantwell Financial seeks to build solid business relationships with those who are looking to partner with a firm for a long term commitment. We are fully aware and accept the fact that over time, financial markets will change positively and negatively. We also understand the proper time allotment that allows us to assist individuals in meeting their desired goals. It is critical that clients also understand, respect and adhere to a multi-year, multi-cycle strategy in order to assure the highest probability for success.</p>
  </div>
  <div class="quote-panel">
    <blockquote>“ As a fee only fiduciary we take great pride in helping people identify their long term financial goals. We then provide the energy required to measure these results over time in order to achieve these goals and objectives. Few firms will provide the service and care we do to work with our clients. ”</blockquote>
    <cite>Brantwell – The steady measurement of progress</cite>
  </div>
</section>

</body>
</html>
```